Cold brew coffee concept

Web site/logo for cold brew coffee served in a keg tap. Cold brew coffee is a natural energy beverage roasted with fair trade/organic beans. Based in New England. Think- Fresh, Natural, Organic, Pure, Mills, Brick, Wood. Ferncastle Coldbrew.

Target Market(s)

Individuals looking for energy drinks without added sugar or dairy. Coffee connoisseurs.

Industry/Entity Type

Trade

Logo Text

Ferncastle Coldbrew

Number of Pages Required

1 page

Font styles to use
Serif

```html
<!DOCTYPE html>
<html lang="en">
<head>
<meta charset="utf-8">
<title>Ferncastle Coldbrew</title>
<link href="https://fonts.googleapis.com/css2?family=Titillium+Web:wght@400;600;700&display=swap" rel="stylesheet">
<style>
:root{
  --ink:#1c1a18;
  --white:#ffffff;
  --nav:rgba(20,16,14,.88);
  --roast-dark:#3a2418;
  --roast-mid:#7a4a2c;
  --roast-light:#b07a4e;
  --sunset-a:#6f6458;
  --sunset-b:#c79a6a;
  --sunset-c:#8b7a68;
  --bean-a:#d9cbb8;
  --bean-b:#a98a6a;
  --amber:#e9a320;
  --amber-dark:#c98510;
}
*{margin:0;padding:0;box-sizing:border-box}
html,body{width:1200px;height:2628px;overflow:hidden;background:var(--white)}
body{position:relative;font-family:"Titillium Web",sans-serif;color:var(--ink)}
.abs{position:absolute}
.center{text-align:center}

/* header */
.hero-photo{left:0;top:0;width:1200px;height:720px;background:radial-gradient(ellipse at 72% 40%,var(--roast-light) 0%,var(--roast-mid) 38%,var(--roast-dark) 100%)}
.nav{left:0;top:0;width:1200px;height:48px;background:var(--nav)}
.nav-brand{left:12px;top:0;width:104px;height:48px;background:#0d0b0a;display:flex;align-items:center;justify-content:center;color:var(--white);font-size:11px;font-weight:600;line-height:1.1;text-align:center}
.nav-links{left:330px;top:0;height:48px;display:flex;gap:46px;align-items:center;list-style:none}
.nav-links li{color:var(--white);font-size:20px;font-weight:600}
.social{left:978px;top:12px;display:flex;gap:14px}
.social span{width:26px;height:26px;border-radius:50%;background:var(--white);display:block}
.hero-mark{left:530px;top:110px;width:360px;height:360px;border:4px solid var(--white);border-radius:50%;display:flex;align-items:center;justify-content:center;color:var(--white);font-size:46px;font-weight:700;line-height:1.15;text-align:center}
.scroll-cue{left:0;top:588px;width:1200px;color:var(--white);font-size:16px}

/* about */
.about-title{left:0;top:810px;width:1200px;font-size:50px;font-weight:700;letter-spacing:1px}
.about-lead{left:140px;top:906px;width:920px;font-size:39px;line-height:1.32}
.diff-title{left:0;top:1172px;width:1200px;font-size:40px;font-weight:700}
.diff-text{left:360px;top:1278px;width:480px;font-size:23px;line-height:1.45}

/* feeds band */
.band-photo{left:0;top:1560px;width:1200px;height:660px;background:linear-gradient(100deg,var(--sunset-a) 0%,var(--sunset-b) 45%,var(--sunset-c) 100%)}
.band-cut{left:0;top:1558px}
.keep{left:0;top:1614px;width:1200px;font-size:15px;font-weight:600}
.feed-title{font-size:15px;font-weight:600;font-style:normal;color:var(--white);text-align:center}
.insta-grid{left:208px;top:1832px;width:224px;height:188px;display:grid;grid-template-columns:1fr 1fr;gap:6px}
.insta-grid div{background:linear-gradient(135deg,#8a5a2e,#d49a4a)}
.blog-photo{left:508px;top:1900px;width:204px;height:180px;background:radial-gradient(circle,#6a8a3a 0%,#4a2a18 70%)}
.tweets{left:800px;top:1836px;width:224px;font-size:13px;line-height:1.55;color:var(--white);text-align:center}
.tweets .hl{color:var(--amber)}
.ribbon{color:var(--white);font-size:13px;font-weight:700;text-align:center}
.ribbon span{position:absolute;left:0;top:14px;width:100%}

/* coffees */
.beans-photo{left:0;top:2220px;width:1200px;height:408px;background:linear-gradient(180deg,var(--bean-b) 0%,var(--bean-a) 30%,#efe6da 60%,var(--bean-a) 100%)}
.coffees-title{left:0;top:2296px;width:1200px;font-size:50px;font-weight:700;letter-spacing:1px}
.coffees-lead{left:140px;top:2394px;width:920px;font-size:39px;line-height:1.32;text-shadow:0 0 8px var(--white)}
</style>
</head>
<body>

<div class="abs hero-photo" role="img" aria-label="Glass of iced cold brew coffee on a rustic wooden table scattered with coffee beans"></div>
<nav class="abs nav">
  <div class="abs nav-brand">Ferncastle<br>Coldbrew</div>
  <ul class="abs nav-links"><li>Home</li><li>About Us</li><li>Coffee</li><li>Blog</li><li>Contact</li></ul>
  <div class="abs social"><span></span><span></span><span></span></div>
</nav>
<div class="abs hero-mark">Ferncastle<br>Coldbrew</div>
<div class="abs scroll-cue center">Scroll down to see more
  <svg width="1200" height="26" viewBox="0 0 1200 26" style="display:block"><polyline points="592,8 600,16 608,8" fill="none" stroke="#fff" stroke-width="2"/></svg>
</div>

<h1 class="abs about-title center">About Us</h1>
<p class="abs about-lead center">Lorem ipsum dolor sit amet, mazi audirenc vituperatoribus quo ea, mel nusquam percit cu, duis suavitate id vel? Ad usu gale iudico.</p>
<h2 class="abs diff-title center">Why we are different?</h2>
<p class="abs diff-text center">Iuvaret recteque ex sea, atqui semper apeirian ut sed. Te nihil liberavisse his! Inso-lens recusabo atomorum ut vim, eu pri error movet omnesque, everti audire an has. Eam ad veniam.</p>

<div class="abs band-photo" role="img" aria-label="Couple at sunset by the water sharing coffee, softly blurred"></div>
<svg class="abs band-cut" width="1200" height="140" viewBox="0 0 1200 140"><polygon points="0,0 1200,0 600,132" fill="#fff"/></svg>
<div class="abs keep center">Keep Scrolling
  <svg width="1200" height="24" viewBox="0 0 1200 24" style="display:block"><polyline points="592,4 600,11 608,4" fill="none" stroke="#1c1a18" stroke-width="2"/><polyline points="592,12 600,19 608,12" fill="none" stroke="#1c1a18" stroke-width="2"/></svg>
</div>

<div class="abs feed-title" style="left:208px;top:1800px;width:224px">Latest Snapshot Pic's</div>
<div class="abs insta-grid" role="img" aria-label="Four recent coffee photos">
  <div></div><div></div><div></div><div></div>
</div>
<div class="abs ribbon" style="left:196px;top:2024px;width:248px;height:76px">
  <svg width="248" height="76" viewBox="0 0 248 76" style="position:absolute;left:0;top:0"><polygon points="0,0 248,0 248,40 124,76 0,40" fill="var(--amber)"/></svg>
  <span>Go on Snapshot</span>
</div>

<div class="abs feed-title" style="left:488px;top:1860px;width:244px">Blog: Freight Gold</div>
<div class="abs blog-photo" role="img" aria-label="Coffee beans with a green coffee leaf"></div>
<div class="abs ribbon" style="left:496px;top:2084px;width:228px;height:72px">
  <svg width="228" height="72" viewBox="0 0 228 72" style="position:absolute;left:0;top:0"><polygon points="0,0 228,0 228,36 114,72 0,36" fill="var(--amber)"/></svg>
  <span>Go on Our Blog</span>
</div>

<div class="abs feed-title" style="left:800px;top:1800px;width:224px">Latest Tweets</div>
<div class="abs tweets">
  <div class="hl">@FCB long weekend</div>
  <div>opening hours this week</div>
  <div>Friday from 9am to 5pm</div>
  <div>Saturday and Sunday</div>
  <div>from 10am to 4pm</div>
  <div>Monday 8am to 4pm</div>
  <div class="hl">08 Jun 2016</div>
</div>
<div class="abs ribbon" style="left:796px;top:2024px;width:232px;height:76px">
  <svg width="232" height="76" viewBox="0 0 232 76" style="position:absolute;left:0;top:0"><polygon points="0,0 232,0 232,40 116,76 0,40" fill="var(--amber)"/></svg>
  <span>Towards Chirpline</span>
</div>

<div class="abs beans-photo" role="img" aria-label="Roasted coffee beans spread across a light wooden surface"></div>
<h2 class="abs coffees-title center">Our Coffees</h2>
<p class="abs coffees-lead center">Lorem ipsum dolor sit amet, mazi audirenc vituperatoribus quo ea, mel nusquam percit cu, duis suavitate id vel? Ad usu gale iudico.</p>

</body>
</html>
```